Commercial construction contractor website.

We need a website that contains About Us, Contact info, Services, Project pictures and Industry News section

Target Market(s)

I'm building industral/flex spaces/commercial.

Industry/Entity Type

Commercial/industrial construction

Coding

Coded - Design and coding required

Number of Pages Required

5+ page

Font styles to use
Other font styles liked:
• The logo font is Microgramma Pro

Requirements
Must have
• Must have correct company name spelling: Halvern Ridge Construction
Nice to have
• I do like to see our logo design implemented in the design
Should not have
• Please do not show big city pictures and business suit people. We are a commercial construction company

```html
<!DOCTYPE html>
<html lang="en">
<head>
<meta charset="utf-8">
<title>Halvern Ridge Construction</title>
<link href="https://fonts.googleapis.com/css2?family=Michroma&family=Arimo:ital,wght@0,400;0,700;1,400&family=Raleway:wght@400;500;600&display=swap" rel="stylesheet">
<style>
:root{
  --navy:#0b2d84;
  --navy-deep:#0a2a78;
  --blue:#1a6fc0;
  --blue-band:#1671bb;
  --ink:#222;
  --muted:#666;
  --soft-bg:#f4f6f9;
  --white:#fff;
  --star:#f0a81c;
}
*{margin:0;padding:0;box-sizing:border-box}
html,body{width:1200px;height:3752px;overflow:hidden}
body{position:relative;background:var(--white);font-family:"Arimo",Arial,sans-serif;color:var(--ink)}
.abs{position:absolute}
.wide{font-family:"Michroma",sans-serif;text-transform:uppercase}

/* header */
.site-header{position:absolute;left:0;top:0;width:1200px;height:131px;background:var(--white);z-index:2}
.main-nav a{position:absolute;top:56px;font-family:"Michroma",sans-serif;font-size:13px;color:#333;text-decoration:none;white-space:nowrap}
.main-nav a.active{color:var(--navy)}
.brand-badge{position:absolute;left:108px;top:-10px;width:210px;height:210px;border-radius:50%;background:var(--white);z-index:3;display:flex;align-items:flex-end;justify-content:center;padding-bottom:62px}
.brand-badge span{font-family:"Michroma",sans-serif;font-size:14px;line-height:1.3;color:var(--navy);text-align:center;text-transform:uppercase}

/* hero */
.hero{position:absolute;left:0;top:131px;width:1200px;height:722px;background:linear-gradient(160deg,#c9b79c 0%,#8b7b68 35%,#5b4d44 65%,#3d3532 100%)}
.hero-panel{position:absolute;left:82px;top:232px;width:435px;height:281px;background:rgba(40,35,35,.55)}
.hero-title{position:absolute;left:110px;top:258px;font-family:"Michroma",sans-serif;font-size:34px;line-height:46px;color:var(--white);text-transform:uppercase}
.hero-text{position:absolute;left:110px;top:362px;width:400px;font-size:17px;line-height:28px;color:var(--white)}
.btn{display:flex;align-items:center;justify-content:center;border-radius:30px;font-family:"Michroma",sans-serif;font-size:13px;text-transform:uppercase;text-decoration:none}
.btn-solid{background:linear-gradient(180deg,#12379a,var(--navy));color:var(--white);box-shadow:0 3px 6px rgba(0,0,0,.25)}
.hero .btn{position:absolute;left:112px;top:436px;width:144px;height:48px}

/* welcome */
.welcome-kicker{left:112px;top:966px;font-size:21px;color:var(--navy)}
.welcome-title{left:112px;top:1003px;font-size:23px;color:var(--blue)}
.welcome-text{left:112px;top:1060px;width:471px;font-size:14px;line-height:26.5px;color:var(--muted);text-align:justify}
.welcome .btn{position:absolute;left:112px;top:1274px;width:144px;height:51px}
.brand-mark{left:666px;top:950px;width:418px;height:364px;display:flex;align-items:center;justify-content:center;flex-direction:column;gap:22px}
.brand-mark .dot{width:120px;height:120px;border-radius:50%;background:linear-gradient(135deg,#1f5fc4,var(--navy))}
.brand-mark span{font-family:"Michroma",sans-serif;font-size:26px;line-height:38px;color:var(--navy);text-align:center;text-transform:uppercase}

/* section headings */
.section-title{left:0;width:1200px;text-align:center;font-size:27px}
.rule{left:570px;width:60px;height:3px}
.section-sub{left:0;width:1200px;text-align:center;font-size:15px}

/* services */
.services{position:absolute;left:0;top:1391px;width:1200px;height:553px;background:linear-gradient(180deg,#1a74bd,#1569b0)}
.service{position:absolute;top:0;width:300px;text-align:center;color:var(--white)}
.service-icon{position:absolute;left:85px;top:213px;width:130px;height:130px;border-radius:50%;border:3px solid var(--white);display:flex;align-items:center;justify-content:center}
.service-icon::before{content:"";position:absolute;inset:6px;border-radius:50%;background:var(--white)}
.service-icon svg{position:relative}
.service h3{position:absolute;top:368px;width:300px;font-family:"Michroma",sans-serif;font-size:17px;font-weight:400}
.service p{position:absolute;top:400px;left:25px;width:250px;font-size:13.5px;line-height:25.5px}

/* projects */
.projects{position:absolute;left:0;top:1944px;width:1200px;height:758px;background:var(--soft-bg)}
.tile{position:absolute;width:300px;height:249px}
.tile-photo{}
.tile-text{background:var(--white);text-align:center}
.tile-text h3{position:absolute;top:44px;width:100%;font-family:"Michroma",sans-serif;font-weight:400;font-size:17px;color:#333}
.tile-text p{position:absolute;top:87px;left:40px;width:220px;font-size:13.5px;line-height:25.5px;color:#555}
.btn-outline{position:absolute;left:84px;top:181px;width:133px;height:41px;border:2px solid var(--navy);color:var(--navy);font-size:11px;background:var(--white)}

/* testimonials */
.card{position:absolute;top:2901px;width:472px;height:264px;background:var(--white);border:1px solid #e4e4e4;box-shadow:0 0 8px rgba(0,0,0,.08)}
.avatar{position:absolute;left:31px;top:20px;width:102px;height:102px;border-radius:50%;background:linear-gradient(160deg,#d9b48d,#8f6545)}
.card h4{position:absolute;left:160px;top:36px;font-family:"Raleway",sans-serif;font-weight:500;font-size:18px;color:#222}
.card .role{position:absolute;left:160px;top:62px;font-family:"Raleway",sans-serif;font-size:14px;color:var(--blue)}
.card .stars{position:absolute;left:160px;top:86px}
.card .quote{position:absolute;left:370px;top:34px}
.card blockquote{position:absolute;left:35px;top:146px;width:410px;font-style:italic;font-size:14px;line-height:25.5px;color:#888;text-align:justify}

/* footer */
.site-footer{position:absolute;left:0;top:3241px;width:1200px;height:511px;background:var(--navy-deep);color:var(--white)}
.footer-nav a{position:absolute;top:57px;transform:translateX(-50%);font-family:"Michroma",sans-serif;font-size:13px;color:var(--white);text-decoration:none;white-space:nowrap}
.divider{position:absolute;left:112px;width:976px;height:1px;background:rgba(255,255,255,.18)}
.footer-heading{position:absolute;top:165px;font-family:"Michroma",sans-serif;font-size:19px}
.field{position:absolute;background:var(--white);color:#333;font-size:12px;padding:10px 12px;height:35px}
.submit{position:absolute;left:112px;top:366px;width:98px;height:34px;background:#1670c4;color:var(--white);font-size:13px;display:flex;align-items:center;justify-content:center}
.contact-row{position:absolute;left:552px}
.contact-row .ring{position:absolute;left:0;top:0;width:44px;height:44px;border-radius:50%;border:2px solid var(--white);display:flex;align-items:center;justify-content:center}
.contact-row b{position:absolute;left:57px;top:4px;font-family:"Raleway",sans-serif;font-weight:600;font-size:14px;white-space:nowrap}
.contact-row small{position:absolute;left:57px;top:24px;font-family:"Raleway",sans-serif;font-size:12.5px;color:#c9d3ee;white-space:nowrap}
.footer-brand{position:absolute;left:830px;top:140px;width:272px;text-align:center}
.footer-brand .dot{width:64px;height:64px;border-radius:50%;background:var(--white);margin:0 auto 20px}
.footer-brand span{font-family:"Michroma",sans-serif;font-size:19px;line-height:24px;text-transform:uppercase}
.social{position:absolute;top:331px;width:36px;height:36px;border-radius:50%;border:2px solid var(--white)}
.copyright{position:absolute;left:0;top:459px;width:1200px;text-align:center;font-size:14px}
</style>
</head>
<body>

<header class="site-header">
  <nav class="main-nav">
    <a class="active" href="#" style="left:533px">HOME</a>
    <a href="#" style="left:628px">ABOUT US</a>
    <a href="#" style="left:760px">SERVICES</a>
    <a href="#" style="left:886px">PROJECT</a>
    <a href="#" style="left:1008px">CONTACT</a>
  </nav>
</header>
<div class="brand-badge"><span>Halvern Ridge<br>Construction</span></div>

<section class="hero" role="img" aria-label="Two site engineers in hard hats overlooking a commercial construction site with rebar and formwork">
  <div class="hero-panel"></div>
  <h1 class="hero-title">Halvern Ridge<br>Construction</h1>
  <p class="hero-text">Sed ut perspiciatis unde omnis iste natus error sit voluptatem accusantium doloremque</p>
  <a class="btn btn-solid" href="#">Read More</a>
</section>

<section class="welcome">
  <h2 class="abs wide welcome-kicker">Welcome To</h2>
  <h2 class="abs wide welcome-title">Halvern Ridge Construction</h2>
  <p class="abs welcome-text">Sed ut perspiciatis unde omnis iste natus error sit voluptatem accusantium doloremque laudantium, totam rem aperiam, eaque ipsa quae ab illo inventore veritatis et quasi architecto beatae vitae dicta sunt explicabo. Nemo enim ipsam voluptatem quia voluptas sit aspernatur aut odit aut fugit, sed quia consequuntur magni dolores eos qui ratione voluptatem sequi nesciunt. Neque porro quisquam est, qui dolorem ipsum quia dolor sit amet, consec tetur, adipisci velit, sed quia non numquam eius modi...</p>
  <a class="btn btn-solid" href="#">Read More</a>
  <div class="abs brand-mark"><div class="dot"></div><span>Halvern Ridge<br>Construction</span></div>
</section>

<section class="services">
  <h2 class="abs wide section-title" style="top:58px;color:var(--white)">Our Services</h2>
  <div class="abs rule" style="top:107px;background:var(--white)"></div>
  <p class="abs section-sub" style="top:130px;color:var(--white)">Sed ut perspiciatis unde omnis iste natus error sit voluptatem accusantium doloremque</p>

  <div class="service" style="left:117px">
    <div class="service-icon"><svg width="64" height="54" viewBox="0 0 64 54" fill="none" stroke="#1671bb" stroke-width="3"><rect x="4" y="4" width="56" height="42"/><path d="M4 14h56M16 14v32M30 24h20v14H30z"/></svg></div>
    <h3>SERVICES 01</h3>
    <p>Sed ut perspiciatis unde omnis iste natus error sit voluptatem accus antium unde doloremque</p>
  </div>
  <div class="service" style="left:449px">
    <div class="service-icon"><svg width="64" height="54" viewBox="0 0 64 54" fill="none" stroke="#1671bb" stroke-width="3"><path d="M18 24a14 14 0 0 1 28 0M14 24h36"/><rect x="6" y="6" width="52" height="40" rx="3"/><path d="M2 48h60"/></svg></div>
    <h3>SERVICES 02</h3>
    <p>Sed ut perspiciatis unde omnis iste natus error sit voluptatem accus antium unde doloremque</p>
  </div>
  <div class="service" style="left:782px">
    <div class="service-icon"><svg width="60" height="60" viewBox="0 0 60 60" fill="none" stroke="#1671bb" stroke-width="3" stroke-linecap="round"><path d="M10 50L42 18M18 10l32 32M38 8a10 10 0 0 0 14 14M8 40l12 12"/></svg></div>
    <h3>SERVICES 03</h3>
    <p>Sed ut perspiciatis unde omnis iste natus error sit voluptatem accus antium unde doloremque</p>
  </div>
</section>

<section class="projects">
  <h2 class="abs wide section-title" style="top:48px;color:var(--navy)">Our Projects</h2>
  <div class="abs rule" style="top:100px;background:var(--blue)"></div>
  <p class="abs section-sub" style="top:122px;color:#333">Sed ut perspiciatis unde omnis iste natus error sit voluptatem accusantium doloremque</p>

  <div class="tile tile-photo" style="left:0;top:190px;width:297px;background:linear-gradient(180deg,#3f67a3,#8a7a5c)" role="img" aria-label="Surveyor with a tripod at a building site with a tower crane"></div>
  <div class="tile tile-text" style="left:297px;top:190px"><h3>PROJECT 01</h3><p>Sed ut perspiciatis unde omnis iste natus error sit voluptatem accusanti um ooremque laudantium</p><a class="btn btn-outline" href="#">Read More</a></div>
  <div class="tile tile-photo" style="left:597px;top:190px;background:linear-gradient(160deg,#d8dde2,#9ea6ad)" role="img" aria-label="Top-down view of workers reviewing plans on a table with tools"></div>
  <div class="tile tile-text" style="left:897px;top:190px;width:303px"><h3>PROJECT 02</h3><p style="left:41px">Sed ut perspiciatis unde omnis iste natus error sit voluptatem accusanti um ooremque laudantium</p><a class="btn btn-outline" href="#" style="left:85px">Read More</a></div>

  <div class="tile tile-text" style="left:0;top:439px;width:297px"><h3>PROJECT 03</h3><p style="left:38px">Sed ut perspiciatis unde omnis iste natus error sit voluptatem accusanti um ooremque laudantium</p><a class="btn btn-outline" href="#" style="left:82px">Read More</a></div>
  <div class="tile tile-photo" style="left:297px;top:439px;background:linear-gradient(180deg,#8aa3bd,#6b6a5e)" role="img" aria-label="Structural frames of buildings under construction"></div>
  <div class="tile tile-text" style="left:597px;top:439px"><h3>PROJECT 04</h3><p>Sed ut perspiciatis unde omnis iste natus error sit voluptatem accusanti um ooremque laudantium</p><a class="btn btn-outline" href="#">Read More</a></div>
  <div class="tile tile-photo" style="left:897px;top:439px;width:303px;background:linear-gradient(160deg,#eef0f2,#c9ccd0)" role="img" aria-label="Hard hat and drawings on a desk during planning"></div>
</section>

<section class="testimonials">
  <h2 class="abs wide section-title" style="top:2754px;color:var(--navy)">Testimonials</h2>
  <div class="abs rule" style="top:2805px;background:var(--blue)"></div>
  <p class="abs section-sub" style="top:2827px;color:#333">Sed ut perspiciatis unde omnis iste natus error sit voluptatem accusantium doloremque</p>

  <article class="card" style="left:112px">
    <div class="avatar" role="img" aria-label="Client portrait"></div>
    <h4>Tom Fairley</h4>
    <div class="role">Sed ut perspiciatis unde</div>
    <svg class="stars" width="84" height="14" viewBox="0 0 84 14" fill="none" stroke="var(--star)" stroke-width="1.2"><g id="st"><path d="M7 1l1.8 3.8 4.1.5-3 2.8.8 4.1L7 10.2 3.3 12.2l.8-4.1-3-2.8 4.1-.5z"/></g><use href="#st" x="17"/><use href="#st" x="34"/><use href="#st" x="51"/><use href="#st" x="68"/></svg>
    <svg class="quote" width="78" height="66" viewBox="0 0 78 66" fill="#e3e3e3"><path d="M2 2h30v34c0 16-8 26-26 28v-10c9-2 12-7 12-14H2zM44 2h30v34c0 16-8 26-26 28v-10c9-2 12-7 12-14H44z"/></svg>
    <blockquote>Sed ut perspiciatis unde omnis iste natus error sit voluptatem accusantium doloremque laudantium, totam rem aperiam, et quasi architecto beatae vitae dicta sunt explicabo.</blockquote>
  </article>
  <article class="card" style="left:616px">
    <div class="avatar" role="img" aria-label="Client portrait"></div>
    <h4>Tom Fairley</h4>
    <div class="role">Sed ut perspiciatis unde</div>
    <svg class="stars" width="84" height="14" viewBox="0 0 84 14" fill="none" stroke="var(--star)" stroke-width="1.2"><use href="#st"/><use href="#st" x="17"/><use href="#st" x="34"/><use href="#st" x="51"/><use href="#st" x="68"/></svg>
    <svg class="quote" width="78" height="66" viewBox="0 0 78 66" fill="#e3e3e3"><path d="M2 2h30v34c0 16-8 26-26 28v-10c9-2 12-7 12-14H2zM44 2h30v34c0 16-8 26-26 28v-10c9-2 12-7 12-14H44z"/></svg>
    <blockquote>Sed ut perspiciatis unde omnis iste natus error sit voluptatem accusantium doloremque laudantium, totam rem aperiam, et quasi architecto beatae vitae dicta sunt explicabo.</blockquote>
  </article>
</section>

<footer class="site-footer">
  <nav class="footer-nav">
    <a href="#" style="left:323px">HOME</a>
    <a href="#" style="left:449px">ABOUT US</a>
    <a href="#" style="left:590px">SERVICES</a>
    <a href="#" style="left:725px">PROJECT</a>
    <a href="#" style="left:861px">CONTACT</a>
  </nav>
  <div class="divider" style="top:126px"></div>

  <h3 class="footer-heading" style="left:112px">CONTACT US</h3>
  <div class="field" style="left:112px;top:215px;width:179px">First Name :</div>
  <div class="field" style="left:301px;top:215px;width:181px">Last Name :</div>
  <div class="field" style="left:112px;top:260px;width:179px">Email :</div>
  <div class="field" style="left:301px;top:260px;width:181px">Phone :</div>
  <div class="field" style="left:112px;top:304px;width:370px;height:52px">Message :</div>
  <div class="submit">SUBMIT</div>

  <h3 class="footer-heading" style="left:561px">ADDRESS</h3>
  <div class="contact-row" style="top:214px">
    <div class="ring"><svg width="16" height="20" viewBox="0 0 16 20" fill="none" stroke="#fff" stroke-width="2"><path d="M8 19s6-6.5 6-11A6 6 0 0 0 2 8c0 4.5 6 11 6 11z"/><circle cx="8" cy="8" r="2"/></svg></div>
    <b>ADDRESS</b><small># Lorem Ipsum Dummy Lorem</small>
  </div>
  <div class="contact-row" style="top:274px">
    <div class="ring"><svg width="18" height="18" viewBox="0 0 24 24" fill="#fff"><path d="M6.6 10.8a15 15 0 0 0 6.6 6.6l2.2-2.2a1 1 0 0 1 1-.25 11.4 11.4 0 0 0 3.6.6 1 1 0 0 1 1 1V20a1 1 0 0 1-1 1A17 17 0 0 1 3 4a1 1 0 0 1 1-1h3.5a1 1 0 0 1 1 1c0 1.25.2 2.45.6 3.6a1 1 0 0 1-.25 1z"/></svg></div>
    <b>PHONE NUMBER</b><small>000-555-0142</small>
  </div>
  <div class="contact-row" style="top:340px">
    <div class="ring"><svg width="18" height="14" viewBox="0 0 18 14" fill="#fff"><path d="M0 0h18v2L9 8 0 2zM0 4l9 6 9-6v10H0z"/></svg></div>
    <b>EMAIL US</b><small>info@halvernridge.example</small>
  </div>

  <div class="footer-brand"><div class="dot"></div><span>Halvern Ridge<br>Construction</span></div>
  <div class="social" style="left:866px" aria-label="Social link"></div>
  <div class="social" style="left:908px" aria-label="Social link"></div>
  <div class="social" style="left:951px" aria-label="Social link"></div>
  <div class="social" style="left:993px" aria-label="Social link"></div>
  <div class="social" style="left:1037px" aria-label="Social link"></div>

  <div class="divider" style="top:429px"></div>
  <p class="copyright">© Copyright 2022 Halvern Ridge Construction.All Rights Reserved</p>
</footer>

</body>
</html>
```